Broschüre für Immobilienmakler
Tolverido hat unsere Vorstellungen erkannt und von Beginn an super umgesetzt. Natürlich waren noch nachträgliche Änderungen und Feinabstimmungen notwendig. Diese wurden wunschgemäß perfektioniert. Man hatte hier wirklich sehr schöne Ideen in den Details ohne den Blick auf das Ganze zu verlieren. Dadurch haben wir jetzt eine perfekte Broschüre erhalten. Das war bestimmt nicht unser letztes Projekt. Vielen Dank
Zielgruppe
Wir sind Immobilienmakler & Home Stager; unsere hauptsächliche Zielgruppe sind Personen, die Ihre Immobilie verkaufen möchten. Die Broschüre soll ein wichtiger Teil der Akquise werden. Wir vermitteln als Immobilienmakler ganz ursprünglich, jedoch bieten wir auch den gesamten Service rund um den Verkauf (Einholung Unterlagen, Präsentieren der Immobilie durch kleine Effekte bis hin zu Entrümpelungen und Renovierung inkl. Einrichtungsbeispiele/Deko). Zudem sind wir jeden Tag (auch Sonn-und Feiertags) für unsere Kunden erreichbar und auch in Terminen. (Eindrücke gibt es auch über unsere Vombalo-Bewertungen)
Aufgabenstellung
Wir möchten einerseits natürlich mit unseren Vorzügen ggü. den 'Standard-Maklern' werben, aber auch genauso professionell den 'Standard-Dienst' ohne Home-Staging anbieten. (Viele Kunden denken schnell, dass wir nur außergewöhnliche und arbeitsintensive Objekte annehmen).
Texte würden wir versuchen zu übernehmen (hier würden wir die vorgesehenen Textfelder der Designer nutzen) und Bilder müssten vermutlich abgesprochen werden, da wir nicht sicher sind, ob unser Material dafür ausreicht. Die Bilder der Homepage liegen hier vor und können gerne zusätzlich gesendet werden.
Unsere Schriftart ist die Museo Sans rounded

```html
<!DOCTYPE html>
<html lang="de">
<head>
<meta charset="utf-8">
<title>Liventa Heim – Broschüre</title>
<link href="https://fonts.googleapis.com/css2?family=Montserrat:wght@400;500;600;700&display=swap" rel="stylesheet">
<style>
:root{
  --bg:#e8e9ec;
  --paper:#ffffff;
  --lilac:#a899bf;
  --lilac-dark:#8e76a8;
  --lilac-light:#dccbee;
  --ink:#2a1f22;
  --photo-interior:#d9d4cf;
  --photo-house:#7a8a6a;
  --photo-beam:#4a4140;
}
*{margin:0;padding:0;box-sizing:border-box}
html,body{width:1200px;height:800px;overflow:hidden;background:var(--bg);font-family:"Montserrat",sans-serif;color:var(--ink)}
.canvas{position:relative;width:1200px;height:800px}
.page{position:absolute;background:var(--paper);overflow:hidden}
.abs{position:absolute}
.block{position:absolute;background:var(--lilac)}
.photo{position:absolute}
.rule{position:absolute;background:var(--ink)}
.heading{position:absolute;font-weight:400;letter-spacing:.22em;line-height:1.3;text-transform:uppercase}
.body{position:absolute;font-weight:500;line-height:1.25}
.icon{position:absolute;width:22px;height:22px}
.brand{position:absolute;font-weight:700;font-size:7px;letter-spacing:.04em;color:var(--ink);display:flex;align-items:center;gap:4px;white-space:nowrap}
.brand-dot{width:10px;height:10px;border-radius:50%;background:var(--lilac)}
.bar{position:absolute;height:6px;background:var(--lilac-light)}
.bar span{display:block;height:100%;background:var(--lilac-dark)}
.legend{position:absolute;display:flex;gap:4px;font-size:3.4px;font-weight:600;line-height:1.25;width:75px;color:#fff}
.legend i{flex:none;width:6px;height:6px}
</style>
</head>
<body>
<div class="canvas">

  <!-- Cover -->
  <section class="page cover" style="left:55px;top:91px;width:209px;height:297px">
    <div class="brand" style="left:140px;top:28px"><span class="brand-dot"></span>LIVENTA HEIM</div>
    <div class="block" style="left:41px;top:54px;width:10px;height:111px"></div>
    <div class="photo" role="img" aria-label="Hand hält ein kleines Hausmodell mit Schlüssel über Vertragsunterlagen" style="left:45px;top:60px;width:119px;height:170px;background:linear-gradient(160deg,#e6e6e8,#c9c9cd 60%,#f2f2f2)"></div>
    <div class="abs" style="right:24px;top:262px;text-align:right">
      <div style="font-size:9px;font-weight:500;letter-spacing:.2em">LIVENTA HEIM</div>
      <div style="font-size:4.6px;letter-spacing:.2em;color:var(--lilac);margin-top:1px">LOREM IPSUM DOLOR</div>
    </div>
  </section>

  <!-- Spread: Dolor sit amet -->
  <section class="page spread-intro" style="left:292px;top:91px;width:414px;height:292px">
    <h2 class="heading" style="left:48px;top:88px;font-size:14.5px">Dolor<br>sit amet</h2>
    <div class="rule" style="left:47px;top:146px;width:2px;height:78px"></div>
    <p class="body" style="left:61px;top:144px;width:122px;font-size:6.3px">Lorem ipsum dolor sit amet, consectetuer adipiscing elit,diam nonummy nibh euismod tincidunt ut laoreet dolore magna aliquam erat volutpat. Ut wisi enim ad minim veniam, quis nostrud exerci tation ullamcorper suscipit lobortis nisl ut aliquip ex ea commodo consequat.</p>
    <div class="block" style="left:207px;top:0;width:207px;height:292px"></div>
    <div class="photo" role="img" aria-label="Helles Wohnzimmer mit Holzboden, Sofa und Sideboard" style="left:243px;top:18px;width:171px;height:139px;background:linear-gradient(180deg,#eeeeec,#e2dcd3 55%,#c8a57d)"></div>
    <h2 class="heading" style="left:237px;top:174px;font-size:14.5px">Dolor<br>sit amet</h2>
    <p class="body" style="left:237px;top:213px;width:110px;font-size:6.3px">Lorem ipsum dolor sit amet, consectetuer adipiscing elit,diam nonummy nibh euismod tincidunt ut laoreet dolore magna aliquam</p>
    <svg class="icon" style="left:368px;top:190px" viewBox="0 0 22 22"><circle cx="11" cy="11" r="11" fill="#fff"/><circle cx="11" cy="11" r="6.5" fill="var(--ink)"/><path d="M9.3 7.5v7M12.7 7.5v7" stroke="#fff" stroke-width="1.2"/></svg>
    <svg class="icon" style="left:368px;top:222px" viewBox="0 0 22 22"><circle cx="11" cy="11" r="11" fill="#fff"/><path d="M5.5 11 11 5.5 16.5 11v5.5h-11z" fill="var(--ink)"/><rect x="9.2" y="11.5" width="3.6" height="5" fill="#fff"/></svg>
    <div class="rule" style="left:207px;top:273px;width:158px;height:2px"></div>
  </section>

  <!-- Spread: Sit amet -->
  <section class="page spread-house" style="left:732px;top:91px;width:414px;height:292px">
    <div class="photo" role="img" aria-label="Dunkles Holzhaus mit Giebel, Hecken und gepflastertem Weg" style="left:12px;top:37px;width:181px;height:217px;background:linear-gradient(180deg,#8fb3e0 0%,#3b3a3a 35%,#5e7c46 60%,#8c8c88 100%)"></div>
    <div class="brand" style="left:338px;top:27px"><span class="brand-dot"></span>LIVENTA</div>
    <div class="rule" style="left:237px;top:51px;width:2px;height:76px"></div>
    <h2 class="heading" style="left:245px;top:48px;font-size:11.5px">Sit amet</h2>
    <p class="body" style="left:245px;top:74px;width:130px;font-size:7.8px;font-weight:400">Lorem ipsum dolor sit amet, consectetur adipiscing elit. Etiam iaculis commodo.</p>
    <div class="block" style="left:207px;top:159px;width:207px;height:133px"></div>
    <div class="abs" style="left:236px;top:178px;width:1.5px;height:20px;background:#fff"></div>
    <p class="body" style="left:243px;top:179px;width:140px;font-size:4.1px;color:#fff">Lorem ipsum dolor sit amet, consectetuer adipiscing elit, sed diam nonummy nibh euismod tincidunt ut laoreet dolore magna aliquam erat volutpat. Ut wisi enim ad minim veniam, quis nostrud exerci tation ullamcorper suscipit lobortis nisl ut aliquip ex ea commodo consequat. Duis autem vel eum iriure dolor in hendrerit in vulputate velit esse molestie consequat, vel illum dolore eu feugiat</p>
    <svg class="icon" style="left:268px;top:253px" viewBox="0 0 22 22"><circle cx="11" cy="11" r="11" fill="#fff"/><circle cx="11" cy="11" r="5.5" fill="none" stroke="var(--ink)" stroke-width="1.4"/><circle cx="11" cy="11" r="2" fill="var(--ink)"/><path d="M11 3.5v4M11 14.5v4M3.5 11h4M14.5 11h4" stroke="var(--ink)" stroke-width="1.2"/></svg>
    <svg class="icon" style="left:301px;top:253px" viewBox="0 0 22 22"><circle cx="11" cy="11" r="11" fill="#fff"/><rect x="7" y="5" width="8" height="12" fill="none" stroke="var(--ink)" stroke-width="1.4"/><path d="M8.8 8.5h4.4M8.8 11h4.4M8.8 13.5h4.4" stroke="var(--ink)" stroke-width="1"/></svg>
    <svg class="icon" style="left:334px;top:253px" viewBox="0 0 22 22"><circle cx="11" cy="11" r="11" fill="#fff"/><path d="M8 8 11 15M14 8 11 15M8 8h6" stroke="var(--ink)" stroke-width="1.2"/><circle cx="8" cy="8" r="2" fill="#fff" stroke="var(--ink)" stroke-width="1.3"/><circle cx="14" cy="8" r="2" fill="#fff" stroke="var(--ink)" stroke-width="1.3"/><circle cx="11" cy="15" r="2" fill="#fff" stroke="var(--ink)" stroke-width="1.3"/></svg>
  </section>

  <!-- Spread: Business -->
  <section class="page spread-business" style="left:55px;top:415px;width:413px;height:293px">
    <div class="photo" role="img" aria-label="Wohnraum mit dunklen Holzbalken, Hängesessel und Fliesenboden" style="left:0;top:32px;width:196px;height:132px;background:linear-gradient(180deg,var(--photo-beam) 0%,#e9e6e1 30%,#d8d4cf 70%,#f3f3f3 100%)"></div>
    <div class="photo" role="img" aria-label="Weiße Wand mit Bilderrahmen, Zimmerpflanze und Sitzbank" style="left:219px;top:32px;width:82px;height:132px;background:linear-gradient(180deg,#f1f0ee,#e4e1dc 70%,#6b5a48)"></div>
    <div class="rule" style="left:309px;top:66px;width:2px;height:75px"></div>
    <p class="body" style="left:322px;top:63px;width:70px;font-size:4.6px;font-weight:600">Lorem ipsum dolor sit amet, consectetur adipiscing elit. Etiam iaculis commodo. Lorem ipsum dolor sit amet, consectetuer adipiscing elit, sed diam nonummy nibh euismod tincidunt ut laoreet dolore magna aliquam erat volutpat. Ut veniam, quis nostrud exerci tation ullamcorper suscipit lobortis nisl ut</p>
    <div class="abs" style="left:27px;top:197px;width:2px;height:76px;background:var(--lilac)"></div>
    <h2 class="heading" style="left:36px;top:193px;font-size:12.5px">Business</h2>
    <p class="body" style="left:36px;top:216px;width:145px;font-size:7.6px;font-weight:400">Lorem ipsum dolor sit amet, consectetur adipiscing elit. Etiam iaculis commodo.</p>
    <div class="block" style="left:207px;top:193px;width:206px;height:100px"></div>
    <div class="bar" style="left:236px;top:217px;width:147px"><span style="width:39px"></span></div>
    <div class="bar" style="left:236px;top:227px;width:147px"><span style="width:63px"></span></div>
    <div class="bar" style="left:236px;top:236px;width:147px"><span style="width:117px"></span></div>
    <div class="legend" style="left:231px;top:256px"><i style="background:var(--lilac-dark)"></i>Lorem ipsum dolor sit amet, consectetur adipiscing elit. Etiam iaculis commod.</div>
    <div class="legend" style="left:313px;top:256px"><i style="background:var(--lilac-light)"></i>Lorem ipsum dolor sit amet, consectetur adipiscing elit. Etiam iaculis commod.</div>
    <div class="abs" style="left:207px;top:278px;width:157px;height:2px;background:#fff"></div>
  </section>

  <!-- Spread: Interior -->
  <section class="page spread-interior" style="left:496px;top:415px;width:414px;height:293px">
    <div class="photo" role="img" aria-label="Flur mit Fenster, Spiegeln, Sessel und lila Teppich" style="left:10px;top:37px;width:179px;height:212px;background:linear-gradient(180deg,#f4f4f4,#dedede 55%,#3a3236 80%,#6e4d6a)"></div>
    <div class="abs" style="left:0;top:279px;width:161px;height:2px;background:var(--lilac)"></div>
    <div class="block" style="left:201px;top:0;width:213px;height:293px"></div>
    <p class="body" style="left:228px;top:40px;width:150px;font-size:6.3px;font-weight:400;color:#fff">Lorem ipsum dolor sit amet, consectetur adipiscing elit. Etiam iaculis commod.</p>
    <div class="abs" style="left:220px;top:72px;width:166px;height:2px;background:#fff"></div>
    <div class="photo" role="img" aria-label="Essbereich mit Holzbalken, weißen Stühlen und Fliesenboden" style="left:223px;top:92px;width:191px;height:157px;background:linear-gradient(180deg,var(--photo-beam) 0%,#6b615b 35%,#e7e3dd 70%,#f2f2f2 100%)"></div>
  </section>

  <!-- Back cover -->
  <section class="page back" style="left:939px;top:415px;width:207px;height:293px">
    <div class="block" style="left:0;top:40px;width:70px;height:137px"></div>
    <div class="brand" style="left:134px;top:29px"><span class="brand-dot"></span>LIVENTA</div>
    <div class="abs" style="right:25px;top:218px;text-align:right">
      <div style="font-size:8.6px;font-weight:700;letter-spacing:.18em">COMPANY NAME</div>
      <div style="font-size:4.4px;font-weight:700;letter-spacing:.2em;margin-top:1px">LOREM IPSUM DOLOR</div>
      <p style="font-size:6.4px;line-height:1.25;margin-top:6px;width:110px">Lorem ipsum dolor sit amet, consectetur adipiscing elit. Etiam iaculis.</p>
    </div>
    <div class="rule" style="left:188px;top:220px;width:2px;height:51px"></div>
  </section>

</div>
</body>
</html>
```